We are in search of a new business card design for our business. We have a Mexican Grocery Store called Tamarindo Market, we would like to see that some have mexican design, but we are open to any type of designs.

Phone: to be announced
Fax: to be announced

Address is:
2465 Calloway Blvd
Harlow Point, MD 21290

Industry/Entity Type

Business

```html
<!DOCTYPE html>
<html lang="en">
<head>
<meta charset="utf-8">
<title>Tamarindo Market – Business Card</title>
<link href="https://fonts.googleapis.com/css2?family=Lato:wght@400;700&display=swap" rel="stylesheet">
<style>
  :root {
    --page-bg: #d9d3cb;
    --card-red: #b8282f;
    --card-red-dark: #8e1419;
    --card-red-light: #cf4a4f;
    --card-clear: #eceae6;
    --card-clear-shade: #d4d1cc;
    --accent-green: #2f7a3b;
    --text-light: #f6ecec;
    --brand-red: #a61d24;
  }
  html, body {
    margin: 0;
    padding: 0;
    width: 1200px;
    height: 970px;
    overflow: hidden;
    background: var(--page-bg);
    font-family: "Lato", sans-serif;
  }
  .canvas {
    position: relative;
    width: 1200px;
    height: 970px;
  }
  .business-card {
    position: absolute;
    left: 100px;
    top: 201px;
    width: 1000px;
    height: 568px;
    border-radius: 22px;
    overflow: hidden;
    box-shadow: 0 14px 40px rgba(60, 40, 30, 0.25);
  }
  .card-art {
    position: absolute;
    inset: 0;
  }
  .contact-side {
    position: absolute;
    left: 48px;
    top: 78px;
    color: var(--text-light);
  }
  .employee-name {
    margin: 0;
    font-size: 33px;
    font-weight: 700;
    letter-spacing: 0.5px;
    line-height: 1.1;
  }
  .employee-title {
    margin: 2px 0 0;
    font-size: 26px;
    font-weight: 400;
  }
  .address {
    margin: 106px 0 0;
    font-size: 26px;
    line-height: 34px;
  }
  .contact-list {
    list-style: none;
    margin: 44px 0 0;
    padding: 0;
    font-size: 26px;
    line-height: 33px;
  }
  .contact-list li {
    display: flex;
    align-items: center;
    gap: 14px;
  }
  .contact-list svg {
    width: 26px;
    height: 22px;
    flex: none;
  }
  .brand {
    position: absolute;
    left: 560px;
    top: 262px;
    width: 360px;
    display: flex;
    align-items: center;
    justify-content: center;
    gap: 14px;
  }
  .brand-dot {
    flex: none;
    width: 24px;
    height: 24px;
    border-radius: 50%;
    background: var(--brand-red);
  }
  .brand-name {
    font-size: 40px;
    font-weight: 700;
    color: var(--brand-red);
    white-space: nowrap;
  }
</style>
</head>
<body>
<main class="canvas">
  <section class="business-card">
    <svg class="card-art" viewBox="0 0 1000 568" preserveAspectRatio="none" aria-hidden="true">
      <defs>
        <linearGradient id="redPanel" x1="0" y1="0" x2="1" y2="0.3">
          <stop offset="0" stop-color="var(--card-red-light)"/>
          <stop offset="0.55" stop-color="var(--card-red)"/>
          <stop offset="1" stop-color="var(--card-red-dark)"/>
        </linearGradient>
        <linearGradient id="clearPanel" x1="0" y1="0" x2="1" y2="1">
          <stop offset="0" stop-color="var(--card-clear)"/>
          <stop offset="1" stop-color="var(--card-clear-shade)"/>
        </linearGradient>
      </defs>
      <rect class="clear-panel" width="1000" height="568" fill="url(#clearPanel)"/>
      <path class="accent-curve" d="M512 0 Q430 284 512 568" fill="none" stroke="var(--accent-green)" stroke-width="5"/>
      <path class="red-panel" d="M0 0 H506 Q424 284 506 568 H0 Z" fill="url(#redPanel)"/>
    </svg>

    <div class="contact-side">
      <h1 class="employee-name">EMPLOYEE NAME</h1>
      <p class="employee-title">Managing Director</p>
      <p class="address">2465 Calloway Blvd<br>Harlow Point, MD 21290</p>
      <ul class="contact-list">
        <li>
          <svg viewBox="0 0 26 22" aria-label="Phone"><path d="M2 7 Q13 0 24 7 L22 10 L18 9 L17 6 Q13 5 9 6 L8 9 L4 10 Z" fill="var(--text-light)"/><rect x="7" y="11" width="12" height="9" rx="2" fill="var(--text-light)"/></svg>
          <span>(01) 2345 6789</span>
        </li>
        <li>
          <svg viewBox="0 0 26 22" aria-label="Fax"><rect x="7" y="1" width="12" height="7" fill="var(--text-light)"/><rect x="2" y="8" width="22" height="9" rx="2" fill="var(--text-light)"/><rect x="7" y="14" width="12" height="7" fill="var(--text-light)" stroke="var(--card-red)" stroke-width="1.5"/></svg>
          <span>(01) 2345 6789</span>
        </li>
        <li>
          <svg viewBox="0 0 26 22" aria-label="Email"><rect x="2" y="3" width="22" height="16" fill="none" stroke="var(--text-light)" stroke-width="2"/><path d="M2 3 L13 12 L24 3 M2 19 L10 10 M24 19 L16 10" fill="none" stroke="var(--text-light)" stroke-width="2"/></svg>
          <span>Info@yourcompany.com</span>
        </li>
      </ul>
    </div>

    <div class="brand">
      <span class="brand-dot"></span>
      <span class="brand-name">Tamarindo Market</span>
    </div>
  </section>
</main>
</body>
</html>
```